www.brevatin.com Sales/Order Page ReDesign

We need a new and amazing design for our sales/order page to attract more costumers and new houses for our portal.

Here is the existing page with the current design: https://www.brevatin.com/sales

We are proud owners of www.sommarhytta.no and www.brevatin.com and we want more holiday home owners to join our page so that we can rent out their holiday homes and increase the number of houses on our portal.

To get more homeowners we need a sales page that can sell our products the best way possible. Therefore we want you too blow us away with a fresh, modern, easy understandable and stylish new sales/order page.

The only restrictions we give when it comes to design is that it needs to fit the existing design of our portals, the top and footer are set. Beside that we are open for everything as long as it at once give the customers impression that this is a good, professional page were they just have to put out their houses.

When it comes to content I have added two documents who include the content to put in here and some guidelines on how to organize the page. Please be creative and add necessary graphics, symbols, background pictures and what ever necessary to make this page look professional and appealing to new costumers.

Looking forward to what suggestions we are given.

We just want to inform that we have updated our brief with a much more concrete description of what content to add on the sale page, and who to structure the content on the page. Hope this helps to make suggestions easier. Looking forward to receive some good contributions.

We would just like to make sure that everyone have understood that we are not asking for a new design suggestion to our portal in general. We are only asking for a redesign of our sales/order page you find here www.brevatin.com/sales. We have to day received some designs for our front page and the design it self was good, but that's not what we are asking for this time and don't want you to use time of something we don't need at the moment. We are looking forward too se some good suggestions.

Reason: Hello. Thanks for all the great contributions we have been given so fare. We haven't been able to respond to all design and are therefore extending the deadline so that we are able to respond to the designs we have been giver and to gov time to make final changes.

Reason: We are extending the deadline to give designers time to give new suggestion based on our latest feedback today.

Reason: Extended so we can receive last design changes.

Target Market(s)

This is a presentation page where we present our product agains new home owner who we what to choose listing there property on or site.

Industry/Entity Type

Sales

Requirements
Must have
• A modern design who calms the costumer down and help them in deciding to chose us, and for them to choose us they need to trust and believe in us. Therefore your main task is to create a page that effectively informs about our product, gets the visitors attentions and make them trust us.
Nice to have
• Examples of good competitors and good order pages we like:

http://www.cabinquest.example/info/lyp?icid=IL___O_Text___top_nav_link
https://www.nestlodge.example/rooms/new
https://www.pearvix.example/phone/compare/
http://www.guestnook.example/host
Should not have
• - Bad design :-). With bad design we mean design that looks like it's made in 2 seconds by a little child.

```html
<!DOCTYPE html>
<html lang="en">
<head>
<meta charset="utf-8">
<title>Brevatin – Flexible advertising</title>
<link href="https://fonts.googleapis.com/css2?family=Cinzel:wght@400;600&family=Open+Sans:wght@400;600;700&display=swap" rel="stylesheet">
<style>
:root{
  --bar:#1e8fd6;
  --bar-dark:#1677b8;
  --page:#e9e9e9;
  --panel:#f4f4f4;
  --panel-line:#d2d2d2;
  --blue:#1d8ad0;
  --ink:#333;
  --muted:#555;
  --grey-band:#cfcfcf;
  --grey-band-dark:#b9b9b9;
  --green:#7cbf3a;
  --green-dark:#5b9a22;
  --red:#d8322a;
  --white:#fff;
}
*{box-sizing:border-box;margin:0;padding:0}
html,body{width:1200px;height:2264px;overflow:hidden}
body{position:relative;background:var(--page);font-family:"Open Sans",Arial,sans-serif;color:var(--ink)}
.abs{position:absolute}

/* top bar */
.topbar{left:0;top:0;width:1200px;height:35px;background:linear-gradient(var(--bar),var(--bar-dark))}
.brand{left:156px;top:0;width:259px;height:110px;background:var(--white);box-shadow:0 2px 6px rgba(0,0,0,.25);display:flex;align-items:center;justify-content:center;gap:12px}
.brand-mark{width:26px;height:26px;background:var(--blue)}
.brand-name{font-family:"Cinzel",serif;font-weight:600;font-size:34px;color:var(--blue)}
.brand-chevron{left:156px;top:96px}
.flags{left:754px;top:10px;display:flex;gap:6px}
.flag{width:30px;height:18px}
.flag-no{background:#c8102e}
.flag-uk{background:#2a3f86}
.signin{left:775px;top:8px;width:143px;height:30px;border-radius:3px;background:linear-gradient(#9fd35c,var(--green-dark));color:var(--white);font-size:13px;font-weight:600;display:flex;align-items:center;padding-left:34px;border:1px solid #4f8a1c}
.signin::after{content:"";position:absolute;right:12px;top:12px;border:5px solid transparent;border-top-color:var(--white)}
.list-link{left:926px;top:9px;color:var(--white);font-size:14px;font-weight:700}

/* main panel */
.panel{left:146px;top:231px;width:906px;height:1686px;background:var(--panel);border:1px solid var(--panel-line);border-radius:8px;box-shadow:0 1px 4px rgba(0,0,0,.08)}
.title{left:398px;top:216px;width:402px;height:40px;background:var(--white);border:2px solid #c9c9c9;font-family:"Cinzel",serif;font-size:27px;color:var(--blue);display:flex;align-items:center;justify-content:center;box-shadow:0 2px 4px rgba(0,0,0,.15)}
.col-head{top:294px;height:58px;background:linear-gradient(#e2e2e2,#bdbdbd);border:1px solid #aaa;font-family:"Cinzel",serif;font-size:24px;color:#444;display:flex;align-items:center;justify-content:center;box-shadow:0 3px 5px rgba(0,0,0,.2)}
.col-head.fix{left:252px;width:251px}
.col-head.commission{left:679px;width:222px;font-size:21px}
.divider{left:599px;top:300px;width:0;height:1560px;border-left:2px dotted #bbb}

.item{display:flex;gap:10px;width:380px}
.icon{flex:none;width:26px;height:26px}
.item-body{font-size:15px;line-height:21px}
.item-title{color:var(--blue);font-weight:600}
.item-title small{color:var(--ink);font-weight:400;font-size:13px}
.item-text{font-size:13px;color:var(--muted);line-height:19px}
.item-title.justify{text-align:justify}
.bullets{list-style:none;margin-top:6px;color:var(--blue);font-weight:600}
.bullets li{line-height:28px;padding-left:22px;position:relative}
.bullets li::before{content:"";position:absolute;left:6px;top:12px;width:5px;height:5px;border-radius:50%;background:var(--blue)}
.note{width:380px;text-align:center;color:var(--blue);font-size:15px;font-weight:600;line-height:24px}

/* announce boxes */
.announce{background:#e8e8e8;border:1px solid #ccc}
.band{height:36px;background:linear-gradient(#d7d7d7,var(--grey-band-dark));font-family:"Cinzel",serif;font-size:19px;color:#333;display:flex;align-items:center;justify-content:center}
.partners{display:flex;align-items:center;height:70px;margin-top:18px}
.partner{flex:1;text-align:center;font-size:17px;font-weight:600;color:var(--blue)}
.partner + .partner{border-left:1px solid #c4c4c4}
.badge{width:104px;height:30px;border-radius:4px;background:var(--blue);margin:0 auto}
.pay-title{text-align:center;color:var(--blue);font-weight:600;font-size:15px;margin-top:16px}
.pay-list{display:grid;grid-template-columns:1fr 1fr;list-style:none;color:var(--blue);font-size:14px;font-weight:600;padding:8px 36px 0 40px}
.pay-list li{position:relative;padding-left:16px;line-height:27px}
.pay-list li::before{content:"";position:absolute;left:2px;top:11px;width:5px;height:5px;border-radius:50%;background:var(--blue)}

.handle{top:1942px;width:12px;height:18px;border:1px solid #999;border-radius:3px;background:#f7f7f7}

/* order table */
.order{left:146px;top:1967px;width:906px;height:320px;background:var(--white);border:1px solid var(--panel-line);border-radius:8px}
.order-title{left:160px;top:1980px;font-size:13px;font-weight:700}
.rule{left:160px;height:1px;background:#ddd;width:880px}
.th{top:2022px;font-size:12px;font-weight:700}
.select{left:231px;top:2048px;width:524px;height:40px;border:1px solid #bbb;border-radius:3px;font-size:14px;padding:9px 10px;background:var(--white)}
.select::after{content:"";position:absolute;right:12px;top:16px;border:5px solid transparent;border-top-color:#555}
.cell{font-size:14px}
.remove{left:882px;top:2056px}
.add-btn{left:810px;top:2164px;width:191px;height:40px;border-radius:4px;background:linear-gradient(#a5d663,var(--green-dark));border:1px solid #4f8a1c;color:var(--white);font-size:14px;font-weight:600;display:flex;align-items:center;justify-content:center;gap:8px}
.add-btn .plus{width:18px;height:18px;border-radius:50%;background:var(--white);color:var(--green-dark);font-weight:700;display:flex;align-items:center;justify-content:center;font-size:15px;line-height:1}
</style>
</head>
<body>

<svg width="0" height="0" style="position:absolute" aria-hidden="true">
  <defs>
    <linearGradient id="tile" x1="0" y1="0" x2="0" y2="1"><stop offset="0" stop-color="#4fb0ea"/><stop offset="1" stop-color="#1677b8"/></linearGradient>
    <symbol id="i-house" viewBox="0 0 26 26"><rect width="26" height="26" rx="4" fill="url(#tile)"/><path d="M5 13 13 6l8 7h-3v7h-4v-5h-2v5H8v-7z" fill="#fff"/></symbol>
    <symbol id="i-card" viewBox="0 0 26 26"><rect width="26" height="26" rx="4" fill="url(#tile)"/><rect x="5" y="6" width="16" height="14" rx="2" fill="#fff"/><path d="M8 10h10M8 13h10M8 16h6" stroke="#1d8ad0" stroke-width="1.5"/></symbol>
    <symbol id="i-chat" viewBox="0 0 26 26"><rect width="26" height="26" rx="4" fill="url(#tile)"/><path d="M5 7h12v8H10l-3 3v-3H5z" fill="#fff"/><path d="M18 10h3v7h-2v2l-2-2h-5" fill="none" stroke="#fff" stroke-width="1.5"/></symbol>
    <symbol id="i-image" viewBox="0 0 26 26"><rect width="26" height="26" rx="4" fill="url(#tile)"/><rect x="5" y="7" width="16" height="12" rx="1" fill="#fff"/><path d="M7 17l4-5 3 3 2-2 3 4z" fill="#1d8ad0"/></symbol>
    <symbol id="i-help" viewBox="0 0 26 26"><rect width="26" height="26" rx="4" fill="url(#tile)"/><path d="M10 10a3 3 0 1 1 4 3c-1 .5-1 1-1 2" fill="none" stroke="#fff" stroke-width="2.2" stroke-linecap="round"/><circle cx="13" cy="19" r="1.4" fill="#fff"/></symbol>
    <symbol id="i-screen" viewBox="0 0 26 26"><rect width="26" height="26" rx="4" fill="url(#tile)"/><rect x="5" y="6" width="16" height="11" rx="1" fill="#fff"/><path d="M10 20h6M13 17v3" stroke="#fff" stroke-width="2"/></symbol>
    <symbol id="i-cal" viewBox="0 0 26 26"><rect width="26" height="26" rx="4" fill="url(#tile)"/><rect x="5" y="7" width="16" height="13" rx="1" fill="#fff"/><path d="M5 10h16" stroke="#1d8ad0" stroke-width="2"/><path d="M9 5v4M17 5v4" stroke="#fff" stroke-width="2"/><path d="M8 13h2M12 13h2M16 13h2M8 16h2M12 16h2" stroke="#1d8ad0" stroke-width="1.5"/></symbol>
  </defs>
</svg>

<header>
  <div class="abs topbar"></div>
  <svg class="abs brand-chevron" width="259" height="60" viewBox="0 0 259 60" aria-hidden="true">
    <polygon points="0,14 129.5,0 259,14 259,40 129.5,24 0,40" fill="#3b3b3b"/>
  </svg>
  <div class="abs brand"><span class="brand-mark"></span><span class="brand-name">Brevatin</span></div>
  <div class="abs flags">
    <div class="flag flag-no" role="img" aria-label="Norwegian language"></div>
    <div class="flag flag-uk" role="img" aria-label="English language"></div>
  </div>
  <div class="abs signin">Sign in</div>
  <div class="abs list-link">List your property</div>
</header>

<main>
  <section class="abs panel"></section>
  <h1 class="abs title">Flexible advertising</h1>
  <div class="abs col-head fix">Fix price</div>
  <div class="abs col-head commission">Commission based</div>
  <div class="abs divider"></div>

  <!-- fixed price column -->
  <div class="abs item" style="left:158px;top:382px"><svg class="icon"><use href="#i-house"/></svg><div class="item-body"><div class="item-title">NOK 7 990 each year, <small>if they have one house</small></div></div></div>
  <div class="abs item" style="left:158px;top:458px"><svg class="icon"><use href="#i-house"/></svg><div class="item-body"><div class="item-title">NOK 5 990 each year, <small>if they have 2 - 3 houses</small></div></div></div>
  <div class="abs item" style="left:158px;top:538px"><svg class="icon"><use href="#i-house"/></svg><div class="item-body"><div class="item-title">NOK 4 990 each year, <small>if they have 3 - 5 houses</small></div></div></div>
  <div class="abs item" style="left:158px;top:618px"><svg class="icon"><use href="#i-house"/></svg><div class="item-body"><div class="item-title">More then 5 houses <small>we want them to contact us</small></div></div></div>
  <div class="abs item" style="left:158px;top:692px"><svg class="icon"><use href="#i-card"/></svg><div class="item-body"><div class="item-title">No limits or fee on bookings</div><div class="item-text">Lorem ipsum dolor sit amet, consectetuer adipiscing elit,</div></div></div>
  <div class="abs item" style="left:158px;top:778px"><svg class="icon"><use href="#i-card"/></svg><div class="item-body"><div class="item-title">No limits or fee on bookings request</div><div class="item-text">Lorem ipsum dolor sit amet, consectetuer adipiscing elit,</div></div></div>
  <div class="abs item" style="left:158px;top:858px"><svg class="icon"><use href="#i-house"/></svg><div class="item-body"><div class="item-title">No commission on bookings</div></div></div>
  <p class="abs note" style="left:200px;top:915px">Transection fee on each booking for<br>4,5% on the amount the tenants pay to us.</p>
  <div class="abs item" style="left:158px;top:1004px"><svg class="icon"><use href="#i-image"/></svg><div class="item-body"><div class="item-title">Unlimited number of images</div><div class="item-text">Lorem ipsum dolor sit amet, consectetuer adipiscing</div></div></div>

  <div class="abs announce" style="left:158px;top:1102px;width:428px;height:206px">
    <div class="band">Including announce on</div>
    <div class="partners"><div class="partner">Sommarhytta.no</div><div class="partner">Brevatin</div></div>
    <div style="border-top:1px solid #d0d0d0;margin:12px 20px 0;padding-top:18px"><div class="badge" role="img" aria-label="Listing partner badge"></div></div>
  </div>

  <!-- commission column -->
  <div class="abs item" style="left:621px;top:382px"><svg class="icon"><use href="#i-house"/></svg><div class="item-body"><div class="item-title">No listing price</div></div></div>
  <div class="abs item" style="left:621px;top:458px;width:400px"><svg class="icon"><use href="#i-house"/></svg><div class="item-body"><div class="item-title">A commission that's depend of how many house they have in total with us:</div>
    <ul class="bullets"><li>1 = 18%</li><li>2 – 3 = 15 %</li><li>3 – 5 = 12 %</li></ul></div></div>
  <div class="abs item" style="left:621px;top:618px"><svg class="icon"><use href="#i-house"/></svg><div class="item-body"><div class="item-title">More then 5 houses <small>we want them to contact us</small></div></div></div>
  <div class="abs item" style="left:621px;top:692px"><svg class="icon"><use href="#i-card"/></svg><div class="item-body"><div class="item-title">No limits or fee on bookings</div><div class="item-text">Lorem ipsum dolor sit amet, consectetuer adipiscing elit,</div></div></div>
  <div class="abs item" style="left:621px;top:778px"><svg class="icon"><use href="#i-card"/></svg><div class="item-body"><div class="item-title">No limits or fee on bookings request</div><div class="item-text">Lorem ipsum dolor sit amet, consectetuer adipiscing elit,</div></div></div>
  <p class="abs note" style="left:640px;top:942px">Transection fee on each booking for<br>4,5% on the amount the tenants pay to us.</p>
  <div class="abs item" style="left:621px;top:1004px"><svg class="icon"><use href="#i-image"/></svg><div class="item-body"><div class="item-title">Unlimited number of images</div><div class="item-text">Lorem ipsum dolor sit amet, consectetuer adipiscing</div></div></div>

  <div class="abs announce" style="left:619px;top:1102px;width:420px;height:319px">
    <div class="band">Including announce on</div>
    <div class="partners" style="height:60px;margin-top:14px"><div class="partner">Sommarhytta.no</div><div class="partner">Brevatin</div></div>
    <div class="band" style="margin-top:21px;font-size:18px">They can by addition marketing on</div>
    <div style="padding-top:16px;background:#f4f4f4;height:188px">
      <div class="badge" role="img" aria-label="Listing partner badge" style="height:34px"></div>
      <p class="pay-title">Where they can pay for:</p>
      <ul class="pay-list"><li>60 days 400 NOK</li><li>240 days 1 300 NOK</li><li>120 days 700 NOK</li><li>1 year 1 900 NOK</li></ul>
    </div>
  </div>

  <!-- shared features -->
  <div class="abs item" style="left:158px;top:1466px;width:410px"><svg class="icon"><use href="#i-help"/></svg><div class="item-body"><div class="item-title justify">Are given an own housing advisor who can help the homeowners in who their best rent out there holiday home.</div></div></div>
  <div class="abs item" style="left:158px;top:1576px;width:410px"><svg class="icon"><use href="#i-chat"/></svg><div class="item-body"><div class="item-title justify">We are handling a communication and hassle from tenants.</div></div></div>
  <div class="abs item" style="left:158px;top:1668px"><svg class="icon"><use href="#i-screen"/></svg><div class="item-body"><div class="item-title">Online bookings</div><div class="item-text">Lorem ipsum dolor sit amet, consectetuer adipiscing elit,<br>Lorem ipsum dolor sit amet, consectetuer adipiscing elit,<br>Lorem ipsum dolor sit amet, consectetuer adipiscing elit,</div></div></div>
  <div class="abs item" style="left:158px;top:1805px"><svg class="icon"><use href="#i-cal"/></svg><div class="item-body"><div class="item-title">Online calendars</div><div class="item-text">Lorem ipsum dolor sit amet, consectetuer adipiscing elit,<br>Lorem ipsum dolor sit amet, consectetuer adipiscing elit,<br>Lorem ipsum dolor sit amet, consectetuer adipiscing elit,</div></div></div>

  <div class="abs item" style="left:621px;top:1466px;width:415px"><svg class="icon"><use href="#i-help"/></svg><div class="item-body"><div class="item-title justify">Are given an own housing advisor who can help the homeowners in who their best rent out there holiday home.</div></div></div>
  <div class="abs item" style="left:621px;top:1576px;width:415px"><svg class="icon"><use href="#i-chat"/></svg><div class="item-body"><div class="item-title justify">We are handling a communication and hassle from tenants.</div></div></div>
  <div class="abs item" style="left:621px;top:1668px"><svg class="icon"><use href="#i-screen"/></svg><div class="item-body"><div class="item-title">Online bookings</div><div class="item-text">Lorem ipsum dolor sit amet, consectetuer adipiscing elit,<br>Lorem ipsum dolor sit amet, consectetuer adipiscing elit,<br>Lorem ipsum dolor sit amet, consectetuer adipiscing elit,</div></div></div>
  <div class="abs item" style="left:621px;top:1805px"><svg class="icon"><use href="#i-cal"/></svg><div class="item-body"><div class="item-title">Online calendars</div><div class="item-text">Lorem ipsum dolor sit amet, consectetuer adipiscing elit,<br>Lorem ipsum dolor sit amet, consectetuer adipiscing elit,<br>Lorem ipsum dolor sit amet, consectetuer adipiscing elit,</div></div></div>

  <div class="abs handle" style="left:372px"></div>
  <div class="abs handle" style="left:812px"></div>

  <!-- order table -->
  <section class="abs order"></section>
  <h2 class="abs order-title">Properties</h2>
  <div class="abs rule" style="top:2008px"></div>
  <div class="abs th" style="left:166px">Property no</div>
  <div class="abs th" style="left:465px">Agreement</div>
  <div class="abs cell" style="left:166px;top:2056px">1</div>
  <div class="abs select">Yearly advertising, includes listing at Markedo.no (4990,-)</div>
  <div class="abs cell" style="left:800px;top:2058px">4 990,00</div>
  <svg class="abs remove" width="14" height="14" viewBox="0 0 14 14" aria-label="Remove"><path d="M2 2l10 10M12 2 2 12" stroke="#d8322a" stroke-width="2.5"/></svg>
  <div class="abs rule" style="top:2100px;left:700px;width:340px"></div>
  <div class="abs cell" style="left:720px;top:2112px;font-weight:700">Total</div>
  <div class="abs cell" style="left:800px;top:2112px">4 990,00</div>
  <div class="abs add-btn"><span class="plus">+</span>Add new property</div>
</main>

</body>
</html>
```